Stonebay Towing Business Card

Towing
Accident towing
Mechanical breakdown
Insurance, salvage and recovery
4wd off road towing
Light & Heavy towing
8347 2516
24 hour business 7 days

Logo can be whole size on front

Industry/Entity Type

Towing/ transport

Contact Information for Business Card

The above

```html
<!DOCTYPE html>
<html lang="en">
<head>
<meta charset="utf-8">
<title>Stonebay Towing – Business Card</title>
<link rel="stylesheet" href="https://fonts.googleapis.com/css2?family=Bebas+Neue&family=Exo+2:wght@700&display=swap">
<style>
  :root {
    --backdrop: #5c060b;
    --card-black: #141414;
    --brand-red: #d41f26;
    --white: #ffffff;
  }
  * { margin: 0; padding: 0; box-sizing: border-box; }
  html, body {
    width: 1200px; height: 1000px; overflow: hidden;
    background: var(--backdrop);
  }
  .canvas { position: relative; width: 1200px; height: 1000px; }

  .card {
    position: absolute; left: 298px; width: 600px;
    overflow: hidden;
  }
  .card--front {
    top: 64px; height: 344px;
    background: var(--card-black);
    display: flex; align-items: center; justify-content: center;
  }
  .card--back {
    top: 505px; height: 342px;
    background: var(--brand-red);
  }

  .wordmark {
    font-family: "Bebas Neue", sans-serif;
    font-weight: 400;
    line-height: 1;
    letter-spacing: 2px;
    white-space: nowrap;
  }
  .card--front .wordmark { font-size: 96px; color: var(--brand-red); }
  .card--back .wordmark {
    position: absolute; top: 42px; left: 0; width: 100%;
    text-align: center; font-size: 66px; color: var(--white);
  }

  .services {
    position: absolute; top: 180px; left: 0; width: 100%;
    text-align: center;
    font-family: "Bebas Neue", sans-serif;
    font-size: 21px; line-height: 26px; letter-spacing: 0.3px;
    color: var(--white);
  }
  .services .sep { display: inline-block; margin: 0 11px; }

  .contact-bar {
    position: absolute; left: 0; bottom: 0; width: 100%; height: 50px;
  }
  .contact-bar__rule {
    position: absolute; left: 0; bottom: 0; width: 100%; height: 5px;
    background: var(--white);
  }
  .phone {
    position: absolute; left: 61px; top: 0; height: 30px;
    display: flex; align-items: center; gap: 10px;
    font-family: "Exo 2", sans-serif; font-weight: 700;
    font-size: 23px; letter-spacing: 1.5px; color: var(--white);
  }
  .phone__icon { width: 29px; height: 29px; }
  .hours-tab {
    position: absolute; right: 0; bottom: 0; width: 290px; height: 50px;
  }
  .hours-tab svg { position: absolute; inset: 0; }
  .hours-tab__text {
    position: absolute; left: 40px; top: 12px; width: 220px; text-align: center;
    font-family: "Exo 2", sans-serif; font-weight: 700;
    font-size: 20px; letter-spacing: 0.5px; color: var(--brand-red);
  }
</style>
</head>
<body>
<main class="canvas">
  <section class="card card--front" aria-label="Business card front">
    <h1 class="wordmark">Stonebay Towing</h1>
  </section>

  <section class="card card--back" aria-label="Business card back">
    <p class="wordmark">Stonebay Towing</p>

    <div class="services">
      <p>Towing<span class="sep">|</span>Accident Towing<span class="sep">|</span>Mechanical Breakdown</p>
      <p>Insurance<span class="sep">|</span>Salvage and Recovery<span class="sep">|</span>4WD Off Road Towing</p>
      <p>Light &amp; Heavy Towing</p>
    </div>

    <div class="contact-bar">
      <div class="phone">
        <svg class="phone__icon" viewBox="0 0 30 30" aria-hidden="true">
          <circle cx="15" cy="15" r="15" fill="#ffffff"/>
          <path d="M10.5 7.5c.6-.4 1.4-.3 1.8.3l1.7 2.6c.4.6.3 1.3-.2 1.8l-1.1 1c.8 1.7 2.1 3 3.8 3.9l1-1.1c.5-.5 1.2-.6 1.8-.2l2.6 1.7c.6.4.8 1.2.3 1.8l-1 1.3c-.6.8-1.7 1.1-2.7.8-4.4-1.4-7.8-4.8-9.2-9.2-.3-1 0-2.1.8-2.7z" fill="#d41f26"/>
        </svg>
        <span>8347 2516</span>
      </div>
      <div class="hours-tab">
        <svg viewBox="0 0 290 50" width="290" height="50" aria-hidden="true">
          <path d="M0 50 C14 50 18 46 22 30 C26 8 32 0 50 0 H226 C244 0 250 8 254 30 C258 46 262 50 290 50 Z" fill="#ffffff"/>
        </svg>
        <span class="hours-tab__text">(24/7 Business)</span>
      </div>
      <div class="contact-bar__rule"></div>
    </div>
  </section>
</main>
</body>
</html>
```